Business Card & Logo

Business Card Design Project & Logo

Need logo for business card

Company name is ZORVA electric bikes USA

Target Market(s)

Consumer

Industry/Entity Type

Sporting Good

Contact Information for Business Card

Electric Bike Business Cards, Flyers, and LOGO.

Font styles to use
Sans Serif

Colors
ffc214
ffcf3e
faa54b
fee18a
f37122

Requirements
Must have
• New look &LOGO

```html
<!DOCTYPE html>
<html lang="en">
<head>
<meta charset="UTF-8">
<title>ZORVA electric bikes USA – Business Card</title>
<link rel="stylesheet" href="https://fonts.googleapis.com/css2?family=Open+Sans:ital,wght@0,700;1,400&display=swap">
<style>
  :root {
    --paper: #ffffff;
    --ink: #1c1c1c;
    --orange: #f37122;
    --art-light: #f4f4f4;
    --art-mid: #dcdcdc;
  }
  html, body {
    margin: 0;
    padding: 0;
    width: 1200px;
    height: 777px;
    overflow: hidden;
    background: var(--paper);
  }
  .card {
    position: relative;
    width: 1200px;
    height: 777px;
    background: var(--paper);
    overflow: hidden;
    font-family: "Open Sans", Arial, sans-serif;
  }
  .brand-mark {
    position: absolute;
    left: 110px;
    top: 145px;
    width: 66px;
    height: 66px;
    background: var(--orange);
  }
  .brand-name {
    position: absolute;
    left: 194px;
    top: 101px;
    margin: 0;
    font-weight: 700;
    font-size: 146px;
    line-height: 1;
    letter-spacing: -3px;
    color: var(--ink);
    white-space: nowrap;
  }
  .detail-lines {
    position: absolute;
    left: 0;
    top: 0;
  }
  .bike-art {
    position: absolute;
    left: 864px;
    top: 479px;
    width: 336px;
    height: 298px;
    background: linear-gradient(170deg, var(--art-light) 0%, var(--art-mid) 100%);
    border-radius: 18px 18px 0 0;
  }
  .tagline-band {
    position: absolute;
    left: 0;
    top: 714px;
  }
  .tagline {
    position: absolute;
    left: 42px;
    top: 719px;
    margin: 0;
    font-style: italic;
    font-weight: 400;
    font-size: 40px;
    line-height: 50px;
    letter-spacing: 0.3em;
    color: var(--orange);
    white-space: nowrap;
  }
</style>
</head>
<body>
  <main class="card">
    <div class="bike-art" role="img" aria-label="Black silhouette of a bicycle frame with saddle and handlebar"></div>

    <span class="brand-mark"></span>
    <h1 class="brand-name">ZORVA</h1>

    <svg class="detail-lines" width="1200" height="777" aria-hidden="true">
      <g stroke="var(--ink)" stroke-width="4">
        <line x1="109" y1="354" x2="404" y2="354"/>
        <line x1="147" y1="397" x2="442" y2="397"/>
        <line x1="185" y1="441" x2="479" y2="441"/>
        <line x1="222" y1="484" x2="517" y2="484"/>
      </g>
    </svg>

    <svg class="tagline-band" width="1200" height="63" aria-hidden="true">
      <polygon points="0,0 895,0 881,63 0,63" fill="var(--ink)"/>
    </svg>
    <p class="tagline">Zorva Electric Bikes in USA</p>
  </main>
</body>
</html>
```